Quillbrook
Quillbrook - Construction
Professional
Dale
Partner
4821 Fennmoor Ave Charlotte, NC 28391
d_q7@zentramail.net
Harriet7 Harriet7
Please use the most current design. you may remove demolition and remediation but please keep the slogan
Can you change construction to Demolition & Remediation?

```html
<!DOCTYPE html>
<html lang="en">
<head>
<meta charset="UTF-8">
<title>Quillbrook – Business Card</title>
<link href="https://fonts.googleapis.com/css2?family=Open+Sans:ital,wght@0,400;0,600;0,700;0,800;1,400;1,600&display=swap" rel="stylesheet">
<style>
  :root {
    --navy: #1f3263;
    --green: #6cc04a;
    --white: #ffffff;
    --stage: #e8e8e6;
    --muted: #c9d1e6;
  }
  * { margin: 0; padding: 0; box-sizing: border-box; }
  html, body {
    width: 1200px; height: 901px; overflow: hidden;
    background: var(--stage);
    font-family: "Open Sans", Arial, sans-serif;
  }
  .canvas {
    position: relative; width: 1200px; height: 901px;
    display: flex; flex-direction: column; align-items: center; justify-content: center; gap: 44px;
  }
  .card {
    position: relative; width: 660px; height: 377px; overflow: hidden;
    background: var(--navy);
    box-shadow: 0 6px 18px rgba(0,0,0,.18);
  }
  .card-shapes { position: absolute; inset: 0; }

  /* back side */
  .card--back { display: flex; align-items: center; justify-content: center; }
  .brand-mark { display: flex; align-items: center; gap: 14px; }
  .brand-mark__square { width: 22px; height: 22px; background: var(--green); }
  .brand-mark__name { font-weight: 800; font-size: 46px; color: var(--white); letter-spacing: .5px; }

  /* front side */
  .front-brand {
    position: absolute; left: 32px; top: 92px;
    display: flex; align-items: center; gap: 9px;
  }
  .front-brand__square { width: 14px; height: 14px; background: var(--green); }
  .front-brand__name { font-weight: 800; font-size: 30px; color: var(--navy); }

  .services { position: absolute; left: 40px; top: 170px; list-style: none; }
  .services li {
    display: flex; align-items: center; gap: 9px;
    font-style: italic; font-size: 12.5px; color: var(--navy); line-height: 23px;
  }
  .services svg { width: 8px; height: 8px; flex: none; }

  .contact { position: absolute; left: 372px; top: 92px; color: var(--white); }
  .contact__name { font-weight: 700; font-size: 34px; line-height: 1; }
  .contact__role { font-size: 11px; color: var(--muted); margin-top: 3px; }
  .contact__address { font-size: 13px; line-height: 18px; margin-top: 26px; }
  .contact__email { font-size: 13px; margin-top: 6px; }
</style>
</head>
<body>
<main class="canvas">

  <section class="card card--back">
    <div class="brand-mark">
      <span class="brand-mark__square"></span>
      <span class="brand-mark__name">Quillbrook</span>
    </div>
  </section>

  <section class="card card--front">
    <svg class="card-shapes" viewBox="0 0 660 377" width="660" height="377" aria-hidden="true">
      <polygon points="0,0 282,0 172,377 0,377" fill="var(--white)"/>
      <polygon points="282,0 316,0 206,377 172,377" fill="var(--green)"/>
    </svg>

    <div class="front-brand">
      <span class="front-brand__square"></span>
      <span class="front-brand__name">Quillbrook</span>
    </div>

    <ul class="services">
      <li><svg viewBox="0 0 8 8"><polygon points="0,0 8,4 0,8" fill="var(--green)"/></svg>Decommissioning</li>
      <li><svg viewBox="0 0 8 8"><polygon points="0,0 8,4 0,8" fill="var(--green)"/></svg>Crane &amp; Rigging</li>
      <li><svg viewBox="0 0 8 8"><polygon points="0,0 8,4 0,8" fill="var(--green)"/></svg>Asset Recovery</li>
      <li><svg viewBox="0 0 8 8"><polygon points="0,0 8,4 0,8" fill="var(--green)"/></svg>Remediation</li>
      <li><svg viewBox="0 0 8 8"><polygon points="0,0 8,4 0,8" fill="var(--green)"/></svg>Demolition</li>
    </ul>

    <div class="contact">
      <p class="contact__name">Dale</p>
      <p class="contact__role">Partner</p>
      <p class="contact__address">4821 Fennmoor Ave<br>Charlotte, NC 28391</p>
      <p class="contact__email">d_q7@zentramail.net</p>
    </div>
  </section>

</main>
</body>
</html>
```